Internet plattform about horses with place for banners

We would like to redesign our website www.paddora.ch. We would like a simple, but modern & elegant design.
Of course the final design will be responive - but we'll start with the desktop design..

-> IMPORTANT: We will need place for 2 BANNERS: one 944x250 pixels and another 300x250px
-> We don't want any big image on the top - this takes too much place. (When we have no banners hired, we can put images of horses in place of the banners)
-> Background should be clear or white
-> Text on buttons should be text and no images
-> I would appreciate a smooth line somewhere that makes the whole design not too "rectangular"

A design we like is: www.brontavi.ch (but don't do exactly the same)
-> see possible disposal of elements for top of the page -> new design.gif

On the startpage the most important are the news, as well as a new classifieds, new events .. exact content is not that important for this contest as we will offer our users possibility of choosing which content they will like.

I just upload some images you could use, but it's not a must.
If you need images, you could also take some ones on http://lumofoto.varo.info/plonek/index.php (it's a friend of mine, so I would pay her the rights if we keep your project)

For this contest I don't expect different designs for mobile phones and don't need a css or anything else, just good ideas. Once we choose a partner this would be another job for you.

(Later, we'll work on the logo ...)

Target Market(s)

Swiss people who like horses and equestrian sports

Industry/Entity Type

Internet

Number of Pages Required

1 page

Font styles to use
Serif

Requirements
Must have
• Place for Maxiboard(944x250px) and halfpage(300x250) banners.
• The look should be modern, elegant and serious but not elitist. We should place banners for banks and other luxury sector, but all horse lovers should feel welcome. It should stay a popular site.
Nice to have
• A light element, a smooth or round line that makes the design not just rectangular...
• The design should leave much place for the information
• We leave the choice of colors open, but I like blue.. but will not be the only person to chose.
• You have the adress of our actual site (so feel free to open it - go on the contact page and send us a message,
Should not have
• no flashing design, no dark background, no big header.

```html
<!DOCTYPE html>
<html lang="en">
<head>
<meta charset="utf-8">
<title>Paddora.ch – Horse platform</title>
<link rel="stylesheet" href="https://fonts.googleapis.com/css2?family=Open+Sans:wght@400;600;700&family=Arimo:wght@400;700&display=swap">
<style>
:root{
  --navy:#15297f;
  --navy-dark:#0f1f66;
  --nav-top:#3358c4;
  --nav-bottom:#1d3a98;
  --sky-top:#1a4fd6;
  --sky-mid:#8fb3e8;
  --field:#6aa83a;
  --text:#444;
  --muted:#777;
  --panel:#f5f5f5;
  --line:#d6d6d6;
  --banner-grey:#c6c6c6;
}
*{box-sizing:border-box;margin:0;padding:0}
html,body{width:1147px;height:1200px;overflow:hidden}
body{position:relative;font-family:Arimo,Arial,sans-serif;color:var(--text)}
.backdrop{position:absolute;inset:0;background:linear-gradient(180deg,var(--sky-top) 0%,#3f78e0 20%,var(--sky-mid) 45%,#b9cfe0 60%,#7fae55 75%,var(--field) 100%)}
.abs{position:absolute}
.logo-box{left:78px;top:0;width:186px;height:126px;background:#fff;display:flex;align-items:center;justify-content:center}
.logo-name{font-family:'Open Sans',sans-serif;font-weight:700;font-size:27px;color:var(--navy)}
.search{left:816px;top:64px;width:167px;height:38px;background:#fff;border-radius:2px;display:flex;align-items:center;justify-content:space-between;padding:0 10px 0 8px;font-size:10px;color:#666}
.lang{left:1008px;top:64px;color:#fff;font-size:12px}
.flags{display:flex;gap:11px;margin-top:9px}
.nav{left:0;top:127px;width:1147px;height:48px;background:linear-gradient(180deg,var(--nav-top),var(--nav-bottom))}
.nav ul{list-style:none;position:absolute;left:96px;top:0;height:48px;display:flex;align-items:center;gap:33px;color:#fff;font-size:12px}
.page{left:78px;top:183px;width:991px;height:951px;background:#fff}
.slider{left:78px;top:183px;width:746px;height:198px;background:linear-gradient(100deg,#5d6c6a 0%,#a87a55 35%,#b9865c 55%,#c9b9a6 80%,#8f9aa0 100%)}
.slide-title{left:90px;top:285px;font-family:'Open Sans',sans-serif;font-weight:700;font-size:24px;color:var(--navy)}
.slide-sub{left:90px;top:318px;font-size:17px;color:#fff}
.slide-bar{left:78px;top:350px;width:746px;height:31px;background:rgba(40,40,40,.55)}
.dots{left:415px;top:361px;display:flex;gap:9px}
.dots i{width:10px;height:10px;border-radius:50%;background:#e6e6e6}
.ad-side{left:832px;top:183px;width:237px;height:198px;background:var(--banner-grey);text-align:center;color:#707070}
.ad-side b{display:block;font-weight:400;font-size:30px;margin-top:62px}
.ad-side span{font-size:14px}
.sidebar{left:824px;top:381px;width:245px;height:623px;background:var(--panel)}
.heading{font-family:'Open Sans',sans-serif;font-weight:700;font-size:15px;color:#222;border-left:3px solid var(--navy);padding-left:9px;line-height:19px}
.intro{left:96px;top:453px;width:696px;font-size:10.4px;line-height:17.4px;color:#555}
.promo{left:92px;top:550px;width:694px;height:265px;background:var(--navy);border-radius:14px}
.col{position:absolute;top:20px;width:190px;color:#fff}
.col h3{font-family:'Open Sans',sans-serif;font-weight:400;font-size:13.5px;letter-spacing:.3px}
.col .pic{width:184px;height:107px;border:3px solid #fff;margin-top:9px}
.col p{font-size:10.4px;line-height:16px;margin-top:10px}
.btn-light{display:inline-block;margin-top:8px;padding:5px 6px;background:#e3e3e3;color:var(--navy);font-size:11.5px;border-radius:3px}
.partners{left:92px;top:856px;width:687px;height:98px;border-top:1px solid var(--line);border-bottom:1px solid var(--line)}
.partner{position:absolute;font-family:'Open Sans',sans-serif;font-weight:700}
.news{left:835px;width:224px;height:151px;background:#fff;border:1px solid #e2e2e2}
.date{position:absolute;left:3px;top:24px;width:30px;height:34px;background:var(--navy);color:#fff;font-size:10px;text-align:center;line-height:14px;padding-top:3px}
.date b{display:block}
.news h4{position:absolute;left:48px;top:24px;width:172px;font-size:11.6px;line-height:17px;color:#333}
.news p{position:absolute;left:48px;top:64px;width:172px;font-size:10.2px;line-height:16px;color:#888}
.btn-dark{position:absolute;right:10px;bottom:0;background:var(--navy);color:#fff;font-size:10.5px;padding:3px 9px}
.field{left:836px;width:219px;height:31px;background:#fff;border:1px solid #e0e0e0;font-size:10px;color:#999;padding:9px 7px}
.submit{left:838px;top:951px;width:82px;height:32px;background:var(--navy);color:#fff;font-size:13px;display:flex;align-items:center;justify-content:center}
.footer{left:93px;top:1031px;width:968px;height:83px;border-radius:16px;background:linear-gradient(180deg,#f2f2f2,#dcdcdc)}
.follow{position:absolute;left:16px;top:41px;font-family:'Open Sans',sans-serif;font-weight:700;font-size:16px;color:var(--navy);display:flex;align-items:center;gap:12px}
.social{display:flex;gap:9px}
.social i{width:24px;height:24px;background:var(--navy);opacity:.85}
.copy{position:absolute;right:14px;top:43px;font-size:11px;color:#666}
</style>
</head>
<body>
<div class="backdrop" role="img" aria-label="Blue sky with clouds over a green meadow and hills"></div>

<div class="abs logo-box"><span class="logo-name">Paddora.ch</span></div>

<div class="abs search">Search..
  <svg width="18" height="18" viewBox="0 0 18 18"><circle cx="7.5" cy="7.5" r="5.5" fill="none" stroke="#555" stroke-width="2"/><line x1="11.5" y1="11.5" x2="16" y2="16" stroke="#555" stroke-width="2.4" stroke-linecap="round"/></svg>
</div>
<div class="abs lang">Language:
  <div class="flags">
    <svg width="20" height="20" viewBox="0 0 20 20" aria-label="German"><clipPath id="c1"><circle cx="10" cy="10" r="10"/></clipPath><g clip-path="url(#c1)"><rect width="20" height="7" fill="#111"/><rect y="7" width="20" height="6" fill="#d00"/><rect y="13" width="20" height="7" fill="#fc0"/></g></svg>
    <svg width="20" height="20" viewBox="0 0 20 20" aria-label="French"><clipPath id="c2"><circle cx="10" cy="10" r="10"/></clipPath><g clip-path="url(#c2)"><rect width="7" height="20" fill="#1f3fb0"/><rect x="7" width="6" height="20" fill="#fff"/><rect x="13" width="7" height="20" fill="#e22"/></g></svg>
  </div>
</div>

<nav class="abs nav">
  <ul>
    <li><svg width="22" height="20" viewBox="0 0 22 20"><path d="M11 1 1 10h3v9h5v-6h4v6h5v-9h3z" fill="#fff"/></svg></li>
    <li>Classified</li><li>horses</li><li>Directory</li><li>calendar</li><li>Horse pictures</li><li>forum</li><li>Links</li><li>Our partners</li><li>contact</li><li>About Paddora</li><li>Login My Paddora</li>
  </ul>
</nav>

<div class="abs page"></div>

<div class="abs slider" role="img" aria-label="Two young riders smiling beside a chestnut horse at a stable"></div>
<div class="abs slide-title">Paddora.ch</div>
<div class="abs slide-sub">Lorem ipsum dolor sit amet.</div>
<div class="abs slide-bar"></div>
<div class="abs dots"><i></i><i></i><i></i><i></i></div>

<div class="abs ad-side"><b>banner</b><span>300 X 250</span></div>
<div class="abs sidebar"></div>

<h1 class="abs heading" style="left:96px;top:406px">Wel come to Paddora.ch</h1>
<p class="abs intro">Lorem ipsum dolor sit amet, consectetur adipiscing elit, sed do eiusmod tempor incididunt ut &nbsp;nisi ut aliquip ex ea commodo consequat. Duis aute irure dolor in reprehenderit in voluptate velit esse cillum dolore eu fugiat nulla pariatur. Sed ut perspiciatis unde omnis iste natus error sit voluptatem accusantium doloremque laudantium. Excepteur sint occaecat cupidatat non proident, sunt in culpa qui officia deserunt mollit anim id est laborum emque laudantium.</p>

<section class="abs promo">
  <div class="col" style="left:24px">
    <h3>LOREM IPSUM</h3>
    <div class="pic" role="img" aria-label="Head of a chestnut horse in a mountain pasture" style="background:linear-gradient(160deg,#8fb0d6,#7a4a2a 55%,#6f8a4a)"></div>
    <p>Lorem ipsum dolor sit amet, consecte-tur adipiscing elit, labore et dolore magna aliqua.</p>
    <span class="btn-light">Read More</span>
  </div>
  <div class="col" style="left:251px">
    <h3>LOREM IPSUM</h3>
    <div class="pic" role="img" aria-label="Young man resting his head against a brown horse" style="background:linear-gradient(160deg,#b9b9b0,#6a4a34 50%,#6a7048)"></div>
    <p>Lorem ipsum dolor sit amet, consecte-tur adipiscing elit, labore et dolore magna aliqua.</p>
    <span class="btn-light">Read More</span>
  </div>
  <div class="col" style="left:481px">
    <h3>LOREM IPSUM</h3>
    <div class="pic" role="img" aria-label="Group of young riders standing with their horses" style="background:linear-gradient(160deg,#a8b8c8,#9a4a4a 45%,#5a6aa0 70%,#5f8a3a)"></div>
    <p>Lorem ipsum dolor sit amet, consecte-tur adipiscing elit, labore et dolore magna aliqua.</p>
    <span class="btn-light">Read More</span>
  </div>
</section>

<div class="abs partners">
  <div class="partner" role="img" aria-label="Partner badge" style="left:4px;top:16px;width:66px;height:66px;border:2px solid #c33;background:#f3f3f3"></div>
  <div class="partner" style="left:172px;top:34px;font-size:19px;color:#4a9a3a;font-weight:400">brontavi.ch</div>
  <div class="partner" style="left:333px;top:32px;font-size:20px;color:#2a8a3a">Tervalo</div>
  <div class="partner" style="left:532px;top:30px;font-size:20px;color:#222">Nordhufa</div>
</div>

<h2 class="abs heading" style="left:840px;top:404px">Latest News</h2>
<article class="abs news" style="top:441px">
  <div class="date"><b>09</b>Nov</div>
  <h4>Lorem ipsum dolor sit amet, consectetur eiusmod.</h4>
  <p>Sed ut perspiciatis unde omnis iste natus error sit voluptatem accusan-tium doloremque.</p>
  <span class="btn-dark" style="bottom:2px">Read More</span>
</article>
<article class="abs news" style="top:592px">
  <div class="date"><b>09</b>Nov</div>
  <h4>Lorem ipsum dolor sit amet, consectetur eiusmod.</h4>
  <p>Sed ut perspiciatis unde omnis iste natus error sit voluptatem accusan-tium doloremque.</p>
  <span class="btn-dark" style="bottom:0">Read More</span>
</article>

<h2 class="abs heading" style="left:840px;top:774px">Contact Us</h2>
<div class="abs field" style="top:803px">Your Name</div>
<div class="abs field" style="top:843px">Email</div>
<div class="abs field" style="top:883px;height:55px">Message</div>
<div class="abs submit">Submit</div>

<footer class="abs footer">
  <div class="follow" style="top:29px">Follow Us
    <div class="social"><i aria-label="Social link"></i><i aria-label="Feed link"></i><i aria-label="Social link"></i><i aria-label="Video link"></i></div>
  </div>
  <div class="copy">Copyright 2014 paddora.ch | All right reserved</div>
</footer>
</body>
</html>
```